Book Cover for a book on Lantern Road Ventures

I am self-publishing my book on Brindlemark and need a book cover made. Below are the details. See attached templates for size we need to use. I also attached a previous cover we had made that I liked. The problem with it was they were two boys helping each other but the book is about women. I'm open to your ideas on the cover though, but I wanted to show you a style I liked as an idea.
Front of Cover
Book Title: Lantern Road Ventures
Book Subtitle: Loose Pages of a Harbor Keeper
Author Name: Mirela T. Dunbar
Add on the Spine of Cover: Lantern Road Ventures and Mirela T. Dunbar
Back of the Cover Text:
Lantern Road Ventures: Loose Pages of a Harbor Keeper is an honest account of a business owner’s experience attempting to navigate the start-up community while also pursuing spiritual growth. Author Mirela Dunbar defines a spiritual entrepreneur as “someone who runs an enterprise with the purpose of growing love rather than material gain.” This book discusses the three dimensions of Lantern Road Ventures:
1. The business is an integral part of the founder’s spiritual journey.
2. Employees working for the spiritual enterprise, whether they know it or not, encounter this company because it's part of their spiritual path.
3. The business itself has a life force of its own and its purpose is to further the kingdom of heaven on earth.
These three dimensions happen simultaneously and work together to produce the greatest possible result. However, this can feel confusing to a founder juggling these dimensions while also trying to manage and run a business. This is not a formulaic self-help book or roadmap. Rather, it is a compilation of personal reflections that often seem at odds with the traditional world of entrepreneurship.
Below the description add my picture (see attached for my picture)
Bio text:
Mirela Dunbar founded Calveta with the vision of ushering in a life-long education system that shifts away from standardization to one that empowers people to live their purpose. In college, Mirela interned for Open Kettle, a women’s empowerment initiative where she recognized her passion for helping people find their voice. Mirela's 20-year journey has come full circle to empowering other female CEOs who are pursuing the path of Lantern Road Ventures.
NOTE: Please note that Brindlemark puts a bar code on the bottom right of the back cover as is noted on the attached template.
Size template is attached to the brief, here are the sizes typed out:
# Description Width (in) Height (in)
1 Full Cover 12.79 9.25
2 Front Cover 6 9
3 Safe Area 5.875 8.75
4 Bleed 0.125 0.125
5 Margin 0.125 0.125
6 Spine 0.54 9
7 Spine Safe Area 0.415 8.75
8 Spine Margin 0.062 0.062
9 Barcode Margin 0.25 0.25
Pre-publication checklist
BRINDLEMARK TIPS for the final cover:
1. Save as a PDF. Your cover must be a single PDF that includes the back cover, spine, and front cover as one image.
2. Flatten all transparencies. These can cause the file to print with missing or distorted content. Consult your software's documentation to learn how.
3. Embed your fonts. Consult your software's documentation to learn how.
4. Remove crop marks, color bars, template text. Crop marks are lines showing where pages should be trimmed. Color bars are strips with a series of patches used to ensure color balance during printing. Also, remove any template text, PDF creation guides, or software references.
5. Ensure your cover image meets the minimum resolution of 300 DPI (dots per inch).
6. Optimize PDFs. Optimization is useful to reduce your file size, allowing for higher performance when transferring, uploading, viewing, and printing the files.
7. Remove file security. Locked or encrypted files will fail review.
Target Market(s)
Women who want to be CEOs or are currently CEOs of companies.
Industry/Entity Type
Entrepreneurship, business, spirituality
Requirements
Must have
- Just the text on the description. A very welcoming feel.
Nice to have
- I like the idea of having a sunrise/sunset in the image somehow like in the example I attached to the brief, but again I'm open.
Should not have
- Please don't put any yoga or meditation poses or hands outstretched. I have a lot of interesting ones that look like my example so if you are going to submit after Saturday 10/29, please only do so if you have a new idea! Thanks!

```html
<!DOCTYPE html>
<html lang="en">
<head>
<meta charset="utf-8">
<title>Lantern Road Ventures — Full Cover</title>
<link rel="stylesheet" href="https://fonts.googleapis.com/css2?family=Bebas+Neue&family=Oswald:wght@300;400&family=Montserrat:wght@400;600&display=swap">
<style>
  :root {
    --stage: #161718;
    --sky-top: #5ec7d2;
    --sky-mid: #9fdde3;
    --sky-bottom: #f6fcfc;
    --rose: #e5325f;
    --ink: #1f2226;
    --rule: #d9aebb;
    --spine-edge: rgba(0, 0, 0, 0.12);
  }
  * { margin: 0; padding: 0; box-sizing: border-box; }
  html, body {
    width: 806px; height: 1200px; overflow: hidden;
    background: var(--stage);
  }
  .cover-spread {
    position: absolute; left: 20px; top: 324px;
    width: 766px; height: 551px;
    display: flex;
    background: linear-gradient(180deg, var(--sky-top) 0%, var(--sky-mid) 55%, var(--sky-bottom) 100%);
  }
  .back-cover, .spine, .front-cover { position: relative; height: 100%; }
  .back-cover { width: 366px; }
  .spine {
    width: 34px;
    border-left: 1px solid var(--spine-edge);
    border-right: 1px solid var(--spine-edge);
  }
  .front-cover { width: 366px; }

  .title-main {
    font-family: "Bebas Neue", "Oswald", sans-serif;
    color: var(--rose); line-height: 0.86; display: block;
  }
  .title-sub {
    font-family: "Bebas Neue", "Oswald", sans-serif;
    color: var(--rose); line-height: 0.9; display: block;
  }

  /* Front */
  .front-title {
    position: absolute; top: 44px; left: 0; right: 0; text-align: center;
  }
  .front-title .title-main { font-size: 86px; letter-spacing: 1px; }
  .front-title .title-sub { font-size: 44px; letter-spacing: 0.5px; margin-top: 6px; }
  .front-illustration {
    position: absolute; left: 112px; top: 190px; width: 150px; height: 184px;
    border-radius: 50% 50% 46% 46% / 42% 42% 58% 58%;
    background: radial-gradient(circle at 55% 62%, #2f79c4 0%, #3a8fd4 45%, rgba(94,199,210,0) 72%),
                radial-gradient(circle at 45% 18%, rgba(229,50,95,0.55) 0%, rgba(229,50,95,0) 40%);
  }
  .subtitle-block {
    position: absolute; top: 400px; left: 58px; width: 250px; text-align: center;
  }
  .subtitle-block .rule { height: 1px; background: var(--rose); opacity: 0.6; }
  .subtitle {
    font-family: "Oswald", sans-serif; font-weight: 400;
    font-size: 15px; letter-spacing: 1.4px; color: var(--ink);
    padding: 7px 0 7px;
  }
  .front-author {
    position: absolute; top: 482px; left: 0; right: 0; text-align: center;
    font-family: "Oswald", sans-serif; font-weight: 400;
    font-size: 28px; letter-spacing: 2.5px; color: var(--ink);
  }

  /* Back */
  .back-title { position: absolute; top: 44px; left: 55px; }
  .back-title .title-main { font-size: 54px; letter-spacing: 0.5px; }
  .back-title .title-sub { font-size: 27px; margin-top: 3px; }
  .back-illustration {
    position: absolute; left: 248px; top: 45px; width: 56px; height: 68px;
    border-radius: 50% 50% 46% 46% / 40% 40% 60% 60%;
    background: radial-gradient(circle at 55% 64%, #2f79c4 0%, #3a8fd4 42%, rgba(94,199,210,0) 72%);
  }
  .blurb {
    position: absolute; top: 134px; left: 27px; width: 311px;
    font-family: "Montserrat", sans-serif; font-size: 7.3px; line-height: 9.1px;
    color: var(--ink); text-align: justify;
  }
  .blurb p { margin-bottom: 8px; }
  .blurb ol { list-style: none; margin-bottom: 8px; font-weight: 600; }
  .blurb li { display: flex; gap: 7px; text-align: left; }
  .blurb li .num { width: 7px; flex: none; }
  .author-photo {
    position: absolute; left: 28px; top: 326px; width: 100px; height: 113px;
    background: linear-gradient(180deg, #7fa06a 0%, #b98a6c 45%, #e4516f 100%);
  }
  .bio-name {
    position: absolute; left: 142px; top: 329px;
    font-family: "Oswald", sans-serif; font-weight: 400;
    font-size: 15px; letter-spacing: 1.2px; color: var(--ink);
  }
  .bio {
    position: absolute; left: 140px; top: 350px; width: 198px;
    font-family: "Montserrat", sans-serif; font-size: 7.3px; line-height: 9.1px;
    color: var(--ink); text-align: justify;
  }

  /* Spine */
  .spine-title, .spine-author {
    position: absolute; left: 0; right: 0;
    writing-mode: vertical-rl; display: flex; align-items: center;
    margin: 0 auto;
  }
  .spine-title {
    top: 46px; font-family: "Bebas Neue", sans-serif;
    font-size: 20px; letter-spacing: 1px; color: var(--rose);
  }
  .spine-icon {
    position: absolute; left: 6px; top: 312px; width: 22px; height: 40px;
    border-radius: 50% 50% 46% 46% / 40% 40% 60% 60%;
    background: radial-gradient(circle at 55% 64%, #2f79c4 0%, #3a8fd4 45%, rgba(94,199,210,0) 74%);
  }
  .spine-author {
    top: 376px; font-family: "Oswald", sans-serif; font-weight: 400;
    font-size: 16px; letter-spacing: 1.5px; color: var(--ink);
  }
</style>
</head>
<body>
  <main class="cover-spread">
    <section class="back-cover">
      <h2 class="back-title">
        <span class="title-main">LANTERN</span>
        <span class="title-sub">ROAD VENTURES</span>
      </h2>
      <div class="back-illustration" role="img" aria-label="Small illustration of a caped businesswoman standing on a globe with a ladder"></div>

      <div class="blurb">
        <p>Lantern Road Ventures: Loose Pages of a Harbor Keeper is an honest account of a business owner’s experience attempting to navigate the start-up community while also pursuing spiritual growth. Author Mirela Dunbar defines a spiritual entrepreneur as “someone who runs an enterprise with the purpose of growing love rather than material gain.” This book discusses the three dimensions of Lantern Road Ventures:</p>
        <ol>
          <li><span class="num">1.</span><span>The business is an integral part of the founder’s spiritual journey.</span></li>
          <li><span class="num">2.</span><span>Employees working for the spiritual enterprise, whether they know it or not, encounter this company because it's part of their spiritual path.</span></li>
          <li><span class="num">3.</span><span>The business itself has a life force of its own and its purpose is to further the kingdom of heaven on earth.</span></li>
        </ol>
        <p>These three dimensions happen simultaneously and work together to produce the greatest possible result. However, this can feel confusing to a founder juggling these dimensions while also trying to manage and run a business. This is not a formulaic self-help book or roadmap. Rather, it is a compilation of personal reflections that often seem at odds with the traditional world of entrepreneurship.</p>
      </div>

      <div class="author-photo" role="img" aria-label="Portrait photograph of the author"></div>
      <h3 class="bio-name">MIRELA T. DUNBAR</h3>
      <p class="bio">Founded Calveta with the vision of ushering in a life-long education system that shifts away from standardization to one that empowers people to live their purpose. In college, Mirela interned for Open Kettle, a women’s empowerment initiative where she recognized her passion for helping people find their voice. Mirela's 20-year journey has come full circle to empowering other female CEOs who are pursuing the path of Lantern Road Ventures.</p>
    </section>

    <section class="spine">
      <span class="spine-title">LANTERN ROAD VENTURES</span>
      <div class="spine-icon" role="img" aria-label="Tiny illustration of a caped businesswoman on a globe"></div>
      <span class="spine-author">MIRELA T. DUNBAR</span>
    </section>

    <section class="front-cover">
      <h1 class="front-title">
        <span class="title-main">LANTERN</span>
        <span class="title-sub">ROAD VENTURES</span>
      </h1>
      <div class="front-illustration" role="img" aria-label="Illustration of a businesswoman in a red cape standing atop a blue globe, a ladder leaning against it, small clouds around"></div>
      <div class="subtitle-block">
        <div class="rule"></div>
        <p class="subtitle">LOOSE PAGES OF A HARBOR KEEPER</p>
        <div class="rule"></div>
      </div>
      <p class="front-author">MIRELA T. DUNBAR</p>
    </section>
  </main>
</body>
</html>
```